Harborpoint Meridian Insurance Services

we are a high end insurance agency we specialize on Auto | Home | Business | Life looking for something professional and luxuries at the same time. if you guys need anything else please let me know.

Auto | Home | Business | Life must be under logo on the back with black background.

i want the back part to be black with our gold logo on it.

Target Market(s)

Auto | Home | Business | Life

Industry/Entity Type

Insurance Broker

Contact Information for Business Card

My logo is gold so a black in the back would be nice.

Font styles to use
Serif

Colors
000000

Requirements
Must have
• Big logo on the back with black background.

```html
<!DOCTYPE html>
<html lang="en">
<head>
<meta charset="utf-8">
<title>Harborpoint Meridian Insurance Services — Business Card</title>
<link rel="stylesheet" href="https://fonts.googleapis.com/css2?family=Libre+Baskerville:wght@400;700&display=swap">
<style>
  :root {
    --stage: #d8d3ca;
    --card: #26282b;
    --gold: #e9c020;
    --gold-deep: #c9a00e;
    --silver: #b9bbbe;
    --ink-light: #e6e6e6;
    --ink-dark: #2a2a2a;
    --serif: "Libre Baskerville", "Times New Roman", serif;
  }
  * { box-sizing: border-box; margin: 0; padding: 0; }
  html, body { width: 1200px; height: 780px; overflow: hidden; }
  body {
    background: var(--stage);
    font-family: var(--serif);
    position: relative;
  }
  .card {
    position: absolute;
    top: 90px;
    width: 350px;
    height: 600px;
    background: var(--card);
    border-radius: 4px;
    box-shadow: 0 10px 30px rgba(0,0,0,.25);
    overflow: hidden;
  }
  .card--front { left: 220px; }
  .card--back { left: 630px; }

  /* Front */
  .brand {
    position: absolute;
    top: 60px; left: 0; right: 0;
    text-align: center;
  }
  .brand__dot {
    display: block;
    width: 64px; height: 64px;
    margin: 0 auto 18px;
    border-radius: 50%;
    background: var(--gold);
  }
  .brand__name {
    color: var(--gold);
    font-weight: 700;
    font-size: 19px;
    line-height: 1.35;
    letter-spacing: .04em;
    text-transform: uppercase;
  }
  .person {
    position: absolute;
    top: 250px; left: 0; right: 0;
    text-align: center;
  }
  .person__name {
    color: var(--gold);
    font-weight: 700;
    font-size: 22px;
    letter-spacing: .04em;
    text-transform: uppercase;
  }
  .person__title {
    color: var(--ink-light);
    font-size: 16px;
    margin-top: 4px;
  }
  .contact {
    position: absolute;
    top: 340px; left: 40px; right: 40px;
    text-align: center;
  }
  .contact__rule {
    height: 1px;
    background: var(--gold-deep);
    margin: 0 0 14px;
  }
  .contact__label {
    color: var(--gold);
    font-weight: 700;
    font-size: 11px;
  }
  .contact__value {
    color: var(--ink-light);
    font-size: 16px;
    margin: 4px 0 14px;
  }
  .contact__value--small { font-size: 13px; }
  .web-band {
    position: absolute;
    left: 0; right: 0; bottom: 0;
    height: 88px;
    background: linear-gradient(180deg, #f0cc2a, var(--gold-deep));
    border-top: 3px solid var(--silver);
    display: flex; align-items: center; justify-content: center;
    color: var(--ink-dark);
    font-size: 15px;
  }

  /* Back */
  .back-brand {
    position: absolute;
    top: 50%; left: 50%;
    width: 540px;
    transform: translate(-50%, -50%) rotate(90deg);
    display: flex; align-items: center; justify-content: center; gap: 22px;
  }
  .back-brand__dot {
    flex: none;
    width: 96px; height: 96px;
    border-radius: 50%;
    background: var(--gold);
  }
  .back-brand__text { display: flex; flex-direction: column; gap: 12px; }
  .back-brand__name {
    color: var(--gold);
    font-weight: 700;
    font-size: 24px;
    line-height: 1.3;
    letter-spacing: .04em;
    text-transform: uppercase;
  }
  .back-brand__services {
    color: var(--silver);
    font-size: 14px;
    letter-spacing: .12em;
    text-transform: uppercase;
    white-space: nowrap;
  }
</style>
</head>
<body>
  <section class="card card--front" aria-label="Business card front">
    <div class="brand">
      <span class="brand__dot"></span>
      <p class="brand__name">Harborpoint Meridian<br>Insurance Services</p>
    </div>
    <div class="person">
      <h1 class="person__name">Daniel Whitford</h1>
      <p class="person__title">Managing Director</p>
    </div>
    <div class="contact">
      <div class="contact__rule"></div>
      <p class="contact__label">Phone</p>
      <p class="contact__value">(01) 4826 3170</p>
      <div class="contact__rule"></div>
      <p class="contact__label">Email</p>
      <p class="contact__value contact__value--small">info@harborpointmeridian.com</p>
    </div>
    <div class="web-band">www.harborpointmeridian.com</div>
  </section>

  <section class="card card--back" aria-label="Business card back">
    <div class="back-brand">
      <span class="back-brand__dot"></span>
      <div class="back-brand__text">
        <p class="back-brand__name">Harborpoint Meridian<br>Insurance Services</p>
        <p class="back-brand__services">Auto | Home | Business | Life</p>
      </div>
    </div>
  </section>
</body>
</html>
```